Velmo (Pathways for company scale) website

My plan is to offer a marketplace where by businesses (SME and Corporates) are able to post specific requirements, be that debt funding advice or other types of advice (legal/accountant) on the velmo website and advisors can seek to 'pitch' to the client.

clients should be anonymous - maybe a specific client number? (this is reduces the risk of bypass) and have the ability to choose the advisor via the advisors profile.

Advisors could potential use there Netlyne profile to auto complete on Velmo - not sure if this is possible or costs involved, however this would be ideal.

I would think Wordpress would be the best platform for this type of platform, however I would be guided by the experts.

I would need any code written in html 5 to allow for various devices (mobile, tablets, desktop)

Logo design is currently being completed also via Sketch Hive and I'm finalising colours ext now, so could provide advice in due course.

additional requirements (medium to longer term)
longer term I would be looking to add addition aspects to the site including algorithms, specific financial calculations, some of which I would be able to complete myself.

similar websites would be:
https://www.taskquill.example.au
http://www.fundoraxi.example.au

Industry/Entity Type

Debt

Coding

Coded - Design and coding required

```html
<!DOCTYPE html>
<html lang="en">
<head>
<meta charset="utf-8">
<title>Velmo – Pathways for company scale</title>
<link rel="stylesheet" href="https://fonts.googleapis.com/css2?family=Open+Sans:wght@400;600;700&family=Dancing+Script:wght@500&display=swap">
<style>
:root{
  --teal:#0b5a7a;
  --teal-dark:#08465f;
  --ink:#1a1a1a;
  --body:#7a7a7a;
  --soft:#f2f2f2;
  --rule:#dcdcdc;
  --footer:#1b1b1b;
  --footer-base:#121212;
  --footer-text:#d8d8d8;
  --white:#ffffff;
}
*{box-sizing:border-box;margin:0;padding:0}
html,body{width:1200px;height:2329px;overflow:hidden}
body{position:relative;background:var(--white);font-family:"Open Sans",Arial,sans-serif;color:var(--body)}
.abs{position:absolute}
.top-rule{left:0;top:0;width:1200px;height:4px;background:var(--teal)}
.brand{left:140px;top:40px;display:flex;align-items:center;gap:10px}
.brand-dot{width:26px;height:26px;border-radius:50%;background:var(--teal)}
.brand-name{font-size:34px;font-weight:600;color:var(--teal);letter-spacing:1px}
.nav{left:597px;top:53px;display:flex;align-items:center;font-size:12px;font-weight:600;color:#222;text-transform:uppercase}
.nav a{color:inherit;text-decoration:none;margin-right:37px}
.nav .active{background:var(--teal);color:var(--white);padding:10px 14px;border-radius:6px;margin-right:26px}
.hero{left:0;top:132px;width:1200px;height:532px;background:linear-gradient(180deg,#d6dde3 0%,#a9b6c0 45%,#3e4a55 100%)}
.hero-caption{left:0;top:523px;width:568px;height:141px;background:rgba(40,48,56,.82);border-top:5px solid var(--teal);color:var(--white);padding:30px 0 0 62px}
.hero-caption h1{font-size:30px;font-weight:400;line-height:1}
.hero-caption p{font-size:20px;margin-top:12px;text-transform:uppercase}
.dots{display:flex;gap:6px;margin-top:16px}
.dots span{width:10px;height:10px;border-radius:50%;background:var(--white)}
.dots span:first-child{background:var(--teal)}
.section-title{left:0;width:1200px;text-align:center;font-size:23px;font-weight:700;color:var(--ink);text-transform:uppercase}
.intro{left:140px;top:755px;width:922px;text-align:center;font-size:12px;line-height:24px}
.step{width:300px;text-align:center}
.step-icon{display:block;margin:0 auto}
.step h3{font-size:17px;font-weight:600;color:var(--ink);margin-top:20px}
.step p{font-size:11px;line-height:20px;width:250px;margin:10px auto 0}
.step a{display:inline-block;margin-top:12px;font-size:12px;font-weight:600;color:var(--teal);text-decoration:none}
.why-band{left:0;top:1121px;width:1200px;height:516px;background:var(--soft)}
.card{top:1225px;width:284px}
.card-photo{width:284px;height:166px}
.card h3{font-size:17px;font-weight:700;color:var(--ink);margin-top:20px;text-transform:uppercase}
.card hr{border:0;border-top:1px solid var(--rule);width:185px;margin-top:10px}
.card p{font-size:11px;line-height:23px;margin-top:14px}
.card .btn{display:inline-block;margin-top:18px;background:var(--teal);color:var(--white);font-size:11px;width:93px;height:40px;line-height:40px;text-align:center;text-decoration:none}
.avatar{left:236px;top:1734px;width:118px;height:118px;border-radius:50%;background:linear-gradient(160deg,#e9e4e1,#8c6c5c);border:3px solid var(--teal)}
.quote{left:390px;top:1757px;width:561px;font-size:12px;line-height:23px}
.signature{left:390px;top:1828px;font-family:"Dancing Script",cursive;font-size:18px;color:var(--teal)}
.partners{left:0;top:1920px;width:1200px;height:116px;border-top:1px solid var(--rule)}
.footer{left:0;top:2036px;width:1200px;height:227px;background:var(--footer);color:var(--footer-text)}
.fcol{top:40px}
.fcol h4{font-size:19px;font-weight:400;color:var(--white);text-transform:uppercase;margin-bottom:15px}
.fcol ul{list-style:none;font-size:12px;line-height:23px}
.fcol.bullets li::before{content:"»";font-size:10px;margin-right:18px;color:#bbb}
.social{display:flex;gap:9px}
.social span{width:30px;height:30px;border:2px solid var(--white);border-radius:50%}
.base{left:0;top:2263px;width:1200px;height:66px;background:var(--footer-base);color:var(--white);font-size:12px;text-align:center;line-height:66px}
</style>
</head>
<body>
<div class="abs top-rule"></div>

<header>
  <div class="abs brand"><span class="brand-dot"></span><span class="brand-name">VELMO</span></div>
  <nav class="abs nav">
    <a class="active" href="#">Home</a>
    <a href="#">About Us</a>
    <a href="#">Services</a>
    <a href="#">Blog</a>
    <a href="#" style="margin-right:0">Contact Us</a>
  </nav>
</header>

<section>
  <div class="abs hero" role="img" aria-label="Photo of three business people in silhouette talking in a bright office"></div>
  <div class="abs hero-caption">
    <h1>MARKETPLACE</h1>
    <p>Consectetuer adipiscing elit aenean</p>
    <div class="dots"><span></span><span></span><span></span></div>
  </div>
</section>

<section>
  <h2 class="abs section-title" style="top:703px">How does Velmo work?</h2>
  <p class="abs intro">Consectetuer adipiscing elit. Aenean commodo ligula eget dolor. Aenean massa. Cum sociis natoque penatibus et magnis dis parturient montes, nascetur ridiculus mus. Donec quam felis, ultricies nec, pellentesque eu, pretium quis, sem. Nulla consequat massa quis enim. Donec pede justo, fringilla vel</p>

  <div class="abs step" style="left:120px;top:821px">
    <svg class="step-icon" width="106" height="106" viewBox="0 0 106 106"><circle cx="53" cy="53" r="51" fill="none" stroke="var(--teal)" stroke-width="2"/><circle cx="53" cy="53" r="46" fill="var(--teal)"/><g fill="#fff"><rect x="35" y="32" width="36" height="9" rx="2"/><rect x="35" y="45" width="36" height="9" rx="2"/><rect x="35" y="58" width="36" height="9" rx="2"/></g><g fill="var(--teal)"><circle cx="40" cy="36.5" r="1.6"/><circle cx="40" cy="49.5" r="1.6"/><circle cx="40" cy="62.5" r="1.6"/></g><rect x="51" y="71" width="4" height="6" fill="#fff"/></svg>
    <h3>CUM SOCIIS NATO</h3>
    <p>Consectetuer adipiscing elit. Aenean commodo ligula eget dolor. Aenean massa. Cum sociis natoque penatibus et magnis dis</p>
    <a href="#">Read More »</a>
  </div>
  <div class="abs step" style="left:446px;top:821px">
    <svg class="step-icon" width="106" height="106" viewBox="0 0 106 106"><circle cx="53" cy="53" r="51" fill="none" stroke="var(--teal)" stroke-width="2"/><circle cx="53" cy="53" r="46" fill="var(--teal)"/><rect x="42" y="28" width="26" height="48" rx="4" fill="none" stroke="#fff" stroke-width="3"/><circle cx="55" cy="50" r="7" fill="none" stroke="#fff" stroke-width="3"/><line x1="60" y1="55" x2="66" y2="61" stroke="#fff" stroke-width="3"/><circle cx="36" cy="50" r="5" fill="#fff"/></svg>
    <h3>CUM SOCIIS NATO</h3>
    <p>Consectetuer adipiscing elit. Aenean commodo ligula eget dolor. Aenean massa. Cum sociis natoque penatibus et magnis dis</p>
    <a href="#">Read More »</a>
  </div>
  <div class="abs step" style="left:764px;top:821px">
    <svg class="step-icon" width="106" height="106" viewBox="0 0 106 106"><circle cx="53" cy="53" r="51" fill="none" stroke="var(--teal)" stroke-width="2"/><circle cx="53" cy="53" r="46" fill="var(--teal)"/><g fill="#fff"><circle cx="53" cy="33" r="6"/><rect x="45" y="40" width="16" height="8" rx="3"/><circle cx="37" cy="62" r="5"/><rect x="30" y="68" width="14" height="7" rx="3"/><circle cx="69" cy="62" r="5"/><rect x="62" y="68" width="14" height="7" rx="3"/></g><path d="M53 48v7M37 55h32M37 55v2M69 55v2" stroke="#fff" stroke-width="2" fill="none"/></svg>
    <h3>CUM SOCIIS NATO</h3>
    <p>Consectetuer adipiscing elit. Aenean commodo ligula eget dolor. Aenean massa. Cum sociis natoque penatibus et magnis dis</p>
    <a href="#">Read More »</a>
  </div>
</section>

<section>
  <div class="abs why-band"></div>
  <h2 class="abs section-title" style="top:1163px">Why choose Velmo</h2>
  <article class="abs card" style="left:140px">
    <div class="card-photo" role="img" aria-label="Photo of a person sketching a flowchart on a glass board" style="background:linear-gradient(135deg,#f4f4f4,#c9b8a8)"></div>
    <h3>Post Requirements</h3><hr>
    <p>Consectetuer adipiscing elit. Aenean commodo ligula eget dolor. Aenean massa. Cum sociis natoque penatibus et magnis dis parturient montes</p>
    <a class="btn" href="#">Read More</a>
  </article>
  <article class="abs card" style="left:455px">
    <div class="card-photo" role="img" aria-label="Photo of a business team meeting around a table with laptops" style="background:linear-gradient(135deg,#e3e6ea,#39414d)"></div>
    <h3>Debt Funding Advice</h3><hr>
    <p>Consectetuer adipiscing elit. Aenean commodo ligula eget dolor. Aenean massa. Cum sociis natoque penatibus et magnis dis parturient montes</p>
    <a class="btn" href="#">Read More</a>
  </article>
  <article class="abs card" style="left:773px">
    <div class="card-photo" role="img" aria-label="Photo of advisors reviewing financial charts on a desk" style="background:linear-gradient(135deg,#26415e,#9fb6cc)"></div>
    <h3>Legal/Accountant</h3><hr>
    <p>Consectetuer adipiscing elit. Aenean commodo ligula eget dolor. Aenean massa. Cum sociis natoque penatibus et magnis dis parturient montes</p>
    <a class="btn" href="#">Read More</a>
  </article>
</section>

<section>
  <h2 class="abs section-title" style="top:1683px">What our client says</h2>
  <svg class="abs" style="left:176px;top:1777px" width="20" height="32" viewBox="0 0 20 32"><path d="M16 2L4 16l12 14" fill="none" stroke="#ccc" stroke-width="3"/></svg>
  <svg class="abs" style="left:1008px;top:1777px" width="20" height="32" viewBox="0 0 20 32"><path d="M4 2l12 14L4 30" fill="none" stroke="#ccc" stroke-width="3"/></svg>
  <div class="abs avatar" role="img" aria-label="Portrait photo of the client"></div>
  <p class="abs quote">Suspendisse laoreet augue iderti wer ollicitudin interdum, loremolo lectusto odio, sed fringilla estero libero sederil orci. Phasellusio ty rhoncus suscipit myli eleifendy. Duis malesuada madefill. tincidunt tortor in placerat. Gibuluki ut ultricies turpis.</p>
  <p class="abs signature">Mara Quell (Designation)</p>
</section>

<section class="abs partners">
  <svg width="1200" height="116" viewBox="0 0 1200 116">
    <g fill="#bdbdbd">
      <circle cx="183" cy="58" r="27"/>
      <path d="M273 32h40v30q0 18-20 24q-20-6-20-24z"/>
      <rect x="380" y="38" width="40" height="40" rx="6"/>
      <ellipse cx="517" cy="58" rx="28" ry="20"/>
      <path d="M632 30l18 14-6 32h-24l-6-32z"/>
      <circle cx="743" cy="58" r="27"/>
      <path d="M840 34h52v26q0 18-26 26q-26-8-26-26z"/>
      <ellipse cx="998" cy="56" rx="48" ry="20"/>
    </g>
  </svg>
</section>

<footer class="abs footer">
  <div class="abs fcol bullets" style="left:140px"><h4>The Company</h4>
    <ul><li>About Velmo</li><li>Directory</li><li>Scrapbooks</li><li>Careers</li><li>Taskquill UK</li></ul></div>
  <div class="abs fcol bullets" style="left:335px"><h4>Support</h4>
    <ul><li>How It Works</li><li>Trust &amp; Safety</li><li>FAQ</li><li>Blog</li></ul></div>
  <div class="abs fcol" style="left:498px"><h4>Contact Us</h4>
    <ul style="padding-left:5px"><li>Customers: 0000 Velmo</li><li>Businesses: (00) 5550 7314</li><li>Email: support@velmo.com.au</li></ul></div>
  <div class="abs fcol bullets" style="left:720px"><h4>Cities</h4>
    <ul><li>Sydney</li><li>Melbourne</li><li>Brisbane</li><li>Perth</li><li>Adelaide</li></ul></div>
  <div class="abs fcol" style="left:872px"><h4>Follow Us</h4>
    <div class="social"><span></span><span></span><span></span><span></span><span></span></div></div>
</footer>
<div class="abs base">Copyright © 2014 Velmo . All Rights Reserved</div>
</body>
</html>
```